Locksmith SmartPhone Web Design Project

I am a locksmith and focus on customers that use their smart phones to find me. I have a static web page that I created myself but it is horrible. See for yourself at www.brevalkeyworks.com.au

I want a cross-platform static site that simply shows the information and with the ability to change minor items like pricing. I want it to be compelling in its look and feel (not overwhelming) but simple. It must have a; click to call button; the ability to install a hit counter from pagetallyo.com; payment information just like the current graphic of card/cash/quidlo (orla/brixalonte only).

This will be hosted on my own server.
Updates

Hello Designers,

I have updated the brief in the must have and nice to have fields.

Thank you all,

Tom.

Hello to all Designers,

There is about 9 days left before the deadline. The overall level of competition is extremely high and I would like to thank all the designers who have submitted so far, 27 submissions in total so far. Excellent work.

If you have submitted already and wish to provide new designs, I am keen to see them. 

Hi guys, time is almost up. Please submit any new designs that you may have. The quality has been excellent so far.

Tom.

Target Market(s)

People who are locked out of their house/shop/office etc.

Industry/Entity Type

Locksmith

Requirements
Must have
• click to call button
hit counter from pagetallyo
payment graphic card/cash/quidlo (orla/brixalonte only)
cross platform compatibility smartphone/phablet
Single column page preferable, can have two columns.
Nice to have
• When the page loads regardless of the mobile device, all info should be presented. In other words no vertical or horizontal scroll bars.
Should not have
• hidden code, advertising, credits etc

```html
<!DOCTYPE html>
<html lang="en">
<head>
<meta charset="utf-8">
<title>Breval Keyworks</title>
<link href="https://fonts.googleapis.com/css2?family=Montserrat:wght@700&family=Oswald:wght@600&family=Arimo:wght@400;700&display=swap" rel="stylesheet">
<style>
  :root {
    --bg-top: #1b5ea6;
    --bg-mid: #124a8f;
    --bg-bottom: #0a2f72;
    --band-dark: #0c2c66;
    --band-edge: #2a6ab5;
    --white: #ffffff;
    --frame: #e9eef7;
    --panel-light: #f4f3fb;
    --panel-lav: #c9cfee;
    --photo-a: #c9b8a3;
    --photo-b: #8a6a4a;
    --red: #d4262b;
    --slate: #3e3e42;
    --green: #1f9a12;
    --chevron: #4f86cf;
  }
  * { margin: 0; padding: 0; box-sizing: border-box; }
  html, body { width: 800px; height: 1200px; overflow: hidden; }
  body {
    position: relative;
    font-family: "Arimo", Arial, sans-serif;
    color: var(--white);
    background: linear-gradient(180deg, var(--bg-top) 0%, var(--bg-mid) 45%, var(--bg-bottom) 100%);
  }
  .site-title {
    position: absolute; top: 22px; left: 0; width: 800px;
    text-align: center;
    font-family: "Montserrat", sans-serif; font-weight: 700;
    font-size: 62px; letter-spacing: 1px; line-height: 80px;
    color: var(--white);
  }
  .offer-banner {
    position: absolute; left: 12px; top: 122px; width: 776px; height: 370px;
    border: 5px solid var(--frame); border-radius: 6px;
    background: linear-gradient(180deg, var(--panel-light) 0%, #eceaf8 55%, var(--panel-lav) 100%);
    overflow: hidden;
  }
  .offer-photo {
    position: absolute; left: 0; top: 0; width: 277px; height: 100%;
    background: linear-gradient(120deg, #e8e8ee 0%, var(--photo-a) 45%, var(--photo-b) 100%);
  }
  .offer-copy {
    position: absolute; left: 290px; right: 0; top: 0; bottom: 0;
    text-align: center;
  }
  .offer-headline, .offer-tagline {
    font-family: "Oswald", sans-serif; font-weight: 600;
    font-size: 62px; line-height: 78px;
  }
  .offer-headline { color: var(--red); margin-top: 24px; }
  .offer-price { color: var(--red); font-family: "Arimo", Arial, sans-serif; font-size: 62px; line-height: 78px; }
  .offer-tagline { color: var(--slate); }
  .band { position: absolute; left: 0; width: 800px; }
  .call-band { top: 508px; height: 116px; }
  .call-link {
    position: absolute; left: 0; top: 524px; width: 800px; height: 66px;
    display: flex; align-items: center; justify-content: center; gap: 10px;
    font-size: 42px; color: var(--white); text-decoration: none;
  }
  .call-number {
    font-weight: 700; font-size: 50px; color: var(--green);
    -webkit-text-stroke: 2px var(--white); paint-order: stroke fill;
  }
  .about { position: absolute; left: 15px; top: 664px; width: 770px; }
  .about h2 { font-size: 35px; font-weight: 700; line-height: 44px; margin-bottom: 20px; }
  .about p { font-size: 19.5px; line-height: 36.5px; text-align: justify; margin-bottom: 12px; }
  .more-toggle { position: absolute; left: 385px; top: 1061px; }
  .menu-band { top: 1106px; height: 94px; }
  .menu-link {
    position: absolute; left: 0; top: 1132px; width: 800px; height: 54px;
    display: flex; align-items: center; justify-content: center; gap: 12px;
    font-size: 35px; font-weight: 700; color: var(--white); text-decoration: none;
  }
</style>
</head>
<body>
  <h1 class="site-title">BREVAL KEYWORKS</h1>

  <section class="offer-banner">
    <div class="offer-photo" role="img" aria-label="Photo of a man locked out, leaning his head against a door"></div>
    <div class="offer-copy">
      <p class="offer-headline">Locked Out?</p>
      <p class="offer-price">$150</p>
      <p class="offer-tagline">Gets You In.</p>
      <p class="offer-tagline">EASY!</p>
    </div>
  </section>

  <svg class="band call-band" viewBox="0 0 800 116" aria-hidden="true">
    <defs>
      <linearGradient id="callFill" x1="0" y1="0" x2="0" y2="1">
        <stop offset="0" stop-color="#0f3674"/>
        <stop offset="1" stop-color="#0a2858"/>
      </linearGradient>
    </defs>
    <path d="M0 2 Q45 2 70 45 Q100 112 175 114 L625 114 Q700 112 730 45 Q755 2 800 2 Z" fill="url(#callFill)" stroke="var(--band-edge)" stroke-width="2"/>
  </svg>
  <a class="call-link" href="tel:0427318095">
    <svg width="34" height="34" viewBox="0 0 24 24" aria-hidden="true"><path fill="#fff" d="M6.6 10.8a15.1 15.1 0 0 0 6.6 6.6l2.2-2.2a1 1 0 0 1 1-.25 11.4 11.4 0 0 0 3.6.57 1 1 0 0 1 1 1V20a1 1 0 0 1-1 1A17 17 0 0 1 3 4a1 1 0 0 1 1-1h3.5a1 1 0 0 1 1 1c0 1.25.2 2.45.57 3.57a1 1 0 0 1-.25 1z"/></svg>
    <span>Click to Call -</span>
    <span class="call-number">0427318095</span>
  </a>

  <section class="about">
    <h2>About us</h2>
    <p>Duis aliquam convallis tellus non auctor. Duis non est turpis. Sed consequat mi auctor nulla viverra et porttitor mauris bibendum. Proin nec eros eu eros pretium laoreet nec non nisl. Sed posuere massa sit amet libero aliquam nec vulputate purus vulputate. Cras nisl massa, feugiat eget dictum sit amet, dapibus sit amet lacus. Mauris elit lorem, elementum a aliquet non, convallis sed justo. Curabitur malesuada rutrum tristique.</p>
    <p>Quisque dapibus metus vel nunc vestibulum sagittis suscipit nulla molestie. Nullam eleifend erat a leo cursus vestibulum.</p>
  </section>

  <svg class="more-toggle" width="30" height="30" viewBox="0 0 30 30" aria-hidden="true">
    <circle cx="15" cy="15" r="14" fill="var(--chevron)"/>
    <path d="M9.5 12.5 L15 18 L20.5 12.5" fill="none" stroke="#fff" stroke-width="3" stroke-linecap="round" stroke-linejoin="round"/>
  </svg>

  <svg class="band menu-band" viewBox="0 0 800 94" aria-hidden="true">
    <path d="M18 96 Q55 4 165 2 L635 2 Q745 4 782 96 Z" fill="var(--band-dark)" stroke="var(--band-edge)" stroke-width="2"/>
  </svg>
  <a class="menu-link" href="#">
    <svg width="40" height="30" viewBox="0 0 40 30" aria-hidden="true"><path d="M4 12 L16 2 L16 8 Q34 8 36 26 Q30 16 16 16 L16 22 Z" fill="#c9ccd4" stroke="#3a3f48" stroke-width="2" stroke-linejoin="round"/></svg>
    <span>Go to Main Menu</span>
  </a>
</body>
</html>
```